Professional Modern Website Design

We are a premium IT services provider to the financial industry based in London. Our company is called Veltra our current holding page is www.veltra-example.co.uk. We require a new website to match our new corporate identity. This project is for the design phase only. Development will be handled in-house. I have attached examples of wire frames we have developed (although open to suggestions for improvement) Our brand document that should demonstrate current brand, inc how we communicate to potential clients and finally mostly completed web-content.
We are looking for designers that can create something that sets us apart from our competitors.
Target Market(s)
IT Decision makers in Finance companies such as; hedge funds, private investment banks etc
Industry/Entity Type
Financial
Number of Pages Required
5+ page
Requirements
Must have
- hexagon elements in the design, unique design.
Nice to have
- Blog and social media feeds
Should not have
- Should not resemble a downloaded template

```html
<!DOCTYPE html>
<html lang="en">
<head>
<meta charset="utf-8">
<title>Veltra – IT Services</title>
<link href="https://fonts.googleapis.com/css2?family=Roboto:wght@300;400;500;700&display=swap" rel="stylesheet">
<style>
:root{
  --orange:#f26522;
  --orange-dark:#d9541a;
  --ink:#222;
  --text:#555;
  --dark:#1e1e1e;
  --footer:#262626;
  --light:#eef0f2;
  --white:#fff;
}
*{box-sizing:border-box;margin:0;padding:0}
html,body{width:1200px;height:2568px;overflow:hidden}
body{font-family:'Roboto',sans-serif;color:var(--text);background:var(--white);position:relative}

/* Hero */
.hero{position:absolute;left:0;top:0;width:1200px;height:410px;
  background:linear-gradient(100deg,#8fa2b3 0%,#c9d3dc 40%,#e9edf1 70%,#d7dde3 100%)}
.topbar{position:absolute;left:0;top:0;width:1200px;height:70px;background:rgba(20,20,20,.88);display:flex;align-items:center;justify-content:space-between;padding:0 60px}
.brand{display:flex;align-items:center;gap:12px;color:var(--white);font-weight:700;font-size:22px;letter-spacing:3px}
.brand-mark{width:26px;height:26px;background:var(--orange)}
.nav{display:flex;list-style:none}
.nav li{font-size:16px;color:var(--white);padding:24px 22px;font-weight:500}
.nav li.active{background:var(--orange)}
.hero-panel{position:absolute;left:90px;top:110px;width:470px;height:240px;background:rgba(20,20,20,.8);padding:30px 34px}
.hero-panel h1{color:var(--orange);font-size:36px;font-weight:500;margin-bottom:14px}
.hero-panel p{color:#eee;font-size:16px;line-height:1.5}
.dots{position:absolute;right:34px;bottom:16px;display:flex;gap:6px}
.dots span{width:9px;height:9px;border-radius:50%;background:#888}
.dots span:first-child{background:var(--white)}

/* Services */
.pillars{position:absolute;left:86px;top:572px;width:236px;height:560px;border:3px solid var(--orange);padding:26px 20px}
.pillars h2{color:var(--orange);font-size:17px;font-weight:500;text-align:center;margin-bottom:16px}
.pillars p{font-size:14px;line-height:1.55;color:var(--orange);margin-bottom:16px}
.service{position:absolute;width:340px;text-align:center}
.service svg{display:block;margin:0 auto}
.service h3{color:var(--ink);font-size:17px;font-weight:700;margin:26px 0 16px;line-height:1.3}
.service p{font-size:14px;line-height:1.5;color:var(--text);padding:0 10px}
.more{display:inline-block;margin-top:26px;background:var(--orange);color:var(--white);font-size:16px;padding:10px 38px}

/* Contact */
.contact{position:absolute;left:0;top:1720px;width:1200px;height:340px;background:var(--light)}
.contact-photo{position:absolute;left:0;top:0;width:620px;height:340px;
  background:linear-gradient(90deg,#8aa6bd 0%,#c7d3dd 45%,#e4d6cb 100%)}
.contact-form{position:absolute;left:656px;top:22px;width:460px}
.contact-form h2{color:#9aa3ab;font-size:22px;font-weight:400;letter-spacing:1px;margin-bottom:18px}
.field{height:36px;background:var(--white);border:1px solid #cfd4d8;margin-bottom:12px;font-size:14px;color:#999;padding:9px 12px}
.field.message{height:96px}
.send{display:inline-block;background:var(--orange);color:var(--white);font-size:14px;font-weight:700;padding:10px 32px}

/* Footer */
.footer{position:absolute;left:0;top:2060px;width:1200px;height:260px;background:var(--footer);color:#ddd}
.office{position:absolute;top:30px;width:360px}
.office h4{color:var(--orange);font-size:16px;font-weight:500;margin-bottom:20px;text-transform:uppercase}
.line{display:flex;gap:12px;font-size:15px;line-height:1.5;margin-bottom:18px}
.line svg{flex:none;margin-top:2px}
.footer-brand{position:absolute;right:90px;top:50px;text-align:center}
.footer-brand .brand{justify-content:center;margin-bottom:30px}
.social{display:flex;gap:14px}
.social span{width:38px;height:38px;border-radius:50%;border:2px solid #999}
.map{position:absolute;left:0;top:2320px;width:1200px;height:220px;background:linear-gradient(180deg,#e6e3dc,#d9d6cf)}
.bottom-bar{position:absolute;left:0;top:2540px;width:1200px;height:28px;background:var(--orange);color:var(--white);font-size:11px;text-align:center;line-height:28px}
</style>
</head>
<body>

<header class="hero">
  <div class="hero-photo" role="img" aria-label="Photo of a business team working together at a laptop" style="position:absolute;inset:0"></div>
  <div class="topbar">
    <div class="brand"><span class="brand-mark"></span>VELTRA</div>
    <ul class="nav">
      <li class="active">Home</li><li>Services</li><li>Partners</li><li>Clients</li><li>Contact</li>
    </ul>
  </div>
  <div class="hero-panel">
    <h1>Our Services</h1>
    <p>Lorem Ipsum is simply dummy text of the printing and typesetting industry. Lorem Ipsum has been the industry's standard dummy text ever since the 1500s, when an unknown printer took a galley of type and scrambled it to make a type specimen book.</p>
    <div class="dots"><span></span><span></span><span></span><span></span></div>
  </div>
</header>

<section>
  <div class="pillars">
    <h2>The Veltra Pillars</h2>
    <p>Lorem Ipsum is simply dummy text of the printing and typesetting industry. Lorem Ipsum has been the industry's standard dummy text ever since the 1500s, when an unknown printer took a galley of type.</p>
    <p>but also the leap into electronic typesetting, remaining essentially unchanged. It was popularised in the 1960s with sages.</p>
    <p>but also the leap into electronic typesetting, remaining essentially unchanged. It was popularised in the 1960s with sages.</p>
  </div>

  <div class="service" style="left:418px;top:572px">
    <svg width="200" height="220" viewBox="0 0 200 220"><polygon points="100,0 195,55 195,165 100,220 5,165 5,55" fill="var(--orange)"/>
      <g fill="none" stroke="#fff" stroke-width="5"><rect x="60" y="70" width="80" height="56" rx="4"/><path d="M85 150h30M100 126v24"/></g></svg>
    <h3>Data Centre &amp; Infrastructure<br>Solution</h3>
    <p>Lorem Ipsum is simply dummy text of the printing and typesetting industry. Lorem Ipsum has been the industry's standard dummy text ever since the 1500s, when an unknown printer took a galley of type and scrambled it to make a type specimen book.</p>
    <span class="more">More</span>
  </div>

  <div class="service" style="left:790px;top:572px">
    <svg width="200" height="220" viewBox="0 0 200 220"><polygon points="100,0 195,55 195,165 100,220 5,165 5,55" fill="var(--orange)"/>
      <g fill="none" stroke="#fff" stroke-width="5"><circle cx="100" cy="110" r="20"/><circle cx="100" cy="110" r="42" stroke-dasharray="16 10"/></g></svg>
    <h3>It Support, Managed &amp;<br>profession service</h3>
    <p>Lorem Ipsum is simply dummy text of the printing and typesetting industry. Lorem Ipsum has been the industry's standard dummy text ever since the 1500s, when an unknown printer took a galley of type and scrambled it to make a type specimen book.</p>
    <span class="more">More</span>
  </div>

  <div class="service" style="left:34px;top:1165px">
    <svg width="200" height="220" viewBox="0 0 200 220"><polygon points="100,0 195,55 195,165 100,220 5,165 5,55" fill="var(--orange)"/>
      <g fill="none" stroke="#fff" stroke-width="5"><circle cx="100" cy="110" r="10"/><circle cx="62" cy="78" r="8"/><circle cx="140" cy="80" r="8"/><circle cx="70" cy="148" r="8"/><circle cx="135" cy="145" r="8"/><path d="M92 103L68 83M108 103l26-17M93 117l-18 25M108 117l21 22"/></g></svg>
    <h3>Voice &amp; data networks</h3>
    <p>Lorem Ipsum is simply dummy text of the printing and typesetting industry. Lorem Ipsum has been the industry's standard dummy text ever since the 1500s, when an unknown printer took a galley of type and scrambled it to make a type specimen book.</p>
    <span class="more">More</span>
  </div>

  <div class="service" style="left:418px;top:1165px">
    <svg width="200" height="220" viewBox="0 0 200 220"><polygon points="100,0 195,55 195,165 100,220 5,165 5,55" fill="var(--orange)"/>
      <path d="M65 135h72a22 22 0 0 0 0-44a30 30 0 0 0-57-6a25 25 0 0 0-15 50z" fill="none" stroke="#fff" stroke-width="5"/></svg>
    <h3>Hosting &amp; Cloud</h3>
    <p>Lorem Ipsum is simply dummy text of the printing and typesetting industry. Lorem Ipsum has been the industry's standard dummy text ever since the 1500s, when an unknown printer took a galley of type and scrambled it to make a type specimen book.</p>
    <span class="more">More</span>
  </div>

  <div class="service" style="left:790px;top:1165px">
    <svg width="200" height="220" viewBox="0 0 200 220"><polygon points="100,0 195,55 195,165 100,220 5,165 5,55" fill="var(--orange)"/>
      <g fill="none" stroke="#fff" stroke-width="5"><rect x="66" y="100" width="68" height="54" rx="5"/><path d="M78 100V84a22 22 0 0 1 44 0v16M100 120v14"/></g></svg>
    <h3>IT security &amp; BMI</h3>
    <p>Lorem Ipsum is simply dummy text of the printing and typesetting industry. Lorem Ipsum has been the industry's standard dummy text ever since the 1500s, when an unknown printer took a galley of type and scrambled it to make a type specimen book.</p>
    <span class="more">More</span>
  </div>
</section>

<section class="contact">
  <div class="contact-photo" role="img" aria-label="Photo of a customer support agent wearing a headset"></div>
  <div class="contact-form">
    <h2>CONTACT VELTRA</h2>
    <div class="field">Name</div>
    <div class="field">Email</div>
    <div class="field message">Message</div>
    <span class="send">SEND</span>
  </div>
</section>

<footer class="footer">
  <div class="office" style="left:86px">
    <h4>London Office</h4>
    <div class="line"><svg width="18" height="22" viewBox="0 0 18 22"><path d="M9 21s-7-8-7-12a7 7 0 0 1 14 0c0 4-7 12-7 12z" fill="#ddd"/><circle cx="9" cy="9" r="3" fill="var(--footer)"/></svg><span>27 Calder Row, Northgate<br>London EC9 4TZ</span></div>
    <div class="line"><svg width="18" height="18" viewBox="0 0 18 18"><path d="M4 1l3 4-2 2a10 10 0 0 0 6 6l2-2 4 3-2 3C8 17 1 10 1 3z" fill="#ddd"/></svg><span>+44 20 7946 0381</span></div>
    <div class="line"><svg width="18" height="14" viewBox="0 0 18 14"><rect x="1" y="1" width="16" height="12" fill="none" stroke="#ddd" stroke-width="2"/><path d="M1 1l8 7 8-7" fill="none" stroke="#ddd" stroke-width="2"/></svg><span>info@veltra-example.co.uk</span></div>
  </div>
  <div class="office" style="left:520px">
    <h4>Essex Office</h4>
    <div class="line"><svg width="18" height="22" viewBox="0 0 18 22"><path d="M9 21s-7-8-7-12a7 7 0 0 1 14 0c0 4-7 12-7 12z" fill="#ddd"/><circle cx="9" cy="9" r="3" fill="var(--footer)"/></svg><span>14 Harrow Yard, Westmere<br>Essex EX1 4QT</span></div>
    <div class="line"><svg width="18" height="18" viewBox="0 0 18 18"><path d="M4 1l3 4-2 2a10 10 0 0 0 6 6l2-2 4 3-2 3C8 17 1 10 1 3z" fill="#ddd"/></svg><span>+44 20 7946 0381</span></div>
    <div class="line"><svg width="18" height="14" viewBox="0 0 18 14"><rect x="1" y="1" width="16" height="12" fill="none" stroke="#ddd" stroke-width="2"/><path d="M1 1l8 7 8-7" fill="none" stroke="#ddd" stroke-width="2"/></svg><span>info@veltra-example.co.uk</span></div>
  </div>
  <div class="footer-brand">
    <div class="brand"><span class="brand-mark"></span>VELTRA</div>
    <div class="social"><span></span><span></span><span></span><span></span></div>
  </div>
</footer>

<div class="map" role="img" aria-label="Street map showing the office locations"></div>
<div class="bottom-bar">© Veltra Limited · Company registered in England and Wales · All rights reserved</div>

</body>
</html>
```